Single Page Timetracking Dashboard Desktop App UI Design (Figma Link required)

Main Idea: a SaaS tool where employees can add their time and project in a playful way. There is a infographics and a list with tasks as well.

Based on the attached concept.png the brief is following:

- check the attached rough scribble
- add own ideas or change things if they add value
- Style: colourful, nerdy, professional saas, modern, beautiful, white space
- Quality expectation: inspiration1+2.png
- I will need a Figma link
- desktop only
- make something fresh and unique

Process:
I need to include 2-3 feedback rounds that will span probably around 7 days

Target Market(s)

Internal Business Tool for a Software Development Company

Industry/Entity Type

IT

Other font styles liked:
• Could be monospace, not a must though

Requirements
Must have
• At least one page; Figma Link to the design;
Nice to have
• Microinterations like drop-down, hover/active colors; functionality specifications
Should not have
• Mobile view

```html
<!DOCTYPE html>
<html lang="en">
<head>
<meta charset="utf-8">
<title>Track your time – Dashboard</title>
<link href="https://fonts.googleapis.com/css2?family=Inter:wght@400;500;600;700&display=swap" rel="stylesheet">
<style>
:root{
  --mauve:#bf86a9;
  --mauve-dark:#a9698f;
  --mauve-soft:#c98fb1;
  --pink:#f48fb8;
  --pink-light:#fbc4d8;
  --pink-pale:#fde4ee;
  --blue:#b3cde6;
  --ink:#2a2a2a;
  --muted:#9a9a9a;
  --line:#e6e6e6;
  --white:#ffffff;
  --stage:#bdbdbd;
}
*{box-sizing:border-box;margin:0;padding:0}
html,body{width:1080px;height:1200px;overflow:hidden;background:var(--stage);font-family:"Inter",sans-serif;color:var(--ink)}
.app{position:absolute;left:117px;top:8px;width:940px;height:1315px;transform:scale(.9);transform-origin:0 0;background:var(--white);overflow:hidden;box-shadow:0 20px 40px rgba(0,0,0,.18)}
.abs{position:absolute}
.sidebar{position:absolute;left:0;top:0;width:78px;height:100%;background:var(--mauve)}
.nav-active{position:absolute;left:15px;top:35px;width:63px;height:38px;background:var(--white);border-radius:19px 0 0 19px}
.nav-icon{position:absolute;left:27px;width:24px;height:24px}
.nav-sep{position:absolute;left:22px;width:34px;height:1px;background:rgba(255,255,255,.45)}
.corner{position:absolute;left:78px;top:0;width:0;height:0}
h2.section-title{position:absolute;font-size:18px;font-weight:600}
.dashed-btn{position:absolute;border:1.5px dashed var(--mauve);border-radius:14px;color:var(--mauve);font-size:12px;font-weight:600;display:flex;align-items:center;justify-content:center;gap:5px}
.card{position:absolute;background:var(--white);border-radius:8px;box-shadow:0 2px 8px rgba(0,0,0,.10)}
/* calendar */
.cal-head{position:absolute;left:40px;top:14px;width:115px;height:34px;background:var(--mauve);border-radius:6px;color:#fff;font-size:18px;font-weight:500;display:flex;align-items:center;justify-content:center}
.cal-arrow{position:absolute;top:18px;width:22px;height:26px;border:1px solid var(--line);border-radius:6px}
.cal-grid{position:absolute;left:8px;top:55px;width:180px;display:grid;grid-template-columns:repeat(7,1fr);row-gap:0;font-size:9px;text-align:center}
.cal-grid span{height:19.7px;line-height:19.7px}
.cal-grid .wd{font-size:6.5px;color:var(--muted);height:18px;border-bottom:1px solid var(--line);margin-bottom:6px}
.cal-grid .out{color:#c9c9c9}
.cal-grid .today{color:#fff;position:relative}
.cal-grid .today::before{content:"";position:absolute;left:50%;top:50%;width:17px;height:17px;margin:-8.5px 0 0 -8.5px;border-radius:50%;background:var(--mauve);z-index:-1}
.cal-grid .today{z-index:1}
/* duration picker */
.chip{position:absolute;width:34px;height:32px;border:1px solid var(--line);border-radius:8px;background:#fff;font-size:10px;display:flex;align-items:center;justify-content:center;box-shadow:0 1px 3px rgba(0,0,0,.06)}
.chip.on{background:var(--mauve);color:#fff;border-color:var(--mauve)}
.minutes-band{position:absolute;left:0;top:103px;width:100%;height:47px;background:var(--pink-pale)}
.total{position:absolute;left:0;width:100%;text-align:center}
.total .big{font-size:22px;font-weight:600;letter-spacing:1px}
.total .units{font-size:8.5px;color:#666}
/* form */
.select{position:absolute;top:15px;height:29px;border:1px solid var(--line);border-radius:6px;font-size:8px;font-weight:600;padding:0 10px;display:flex;align-items:center;justify-content:space-between}
.note{position:absolute;left:15px;top:54px;width:284px;height:58px;background:var(--pink-pale);border-radius:6px;font-size:7.5px;font-weight:600;padding:10px}
.log{position:absolute;left:15px;top:120px;width:284px;font-size:6.8px;border-collapse:collapse}
.log th{font-weight:400;color:#aaa;text-align:left;padding:3px 4px;border-bottom:1px solid var(--line)}
.log td{padding:3.6px 4px;border-bottom:1px solid var(--line);color:#444}
/* statistic */
.stat-band{position:absolute;left:78px;top:296px;width:798px;height:321px;background:var(--mauve);border-radius:0 8px 8px 0}
.stat-title{color:#fff}
.dashed-btn.light{border-color:rgba(255,255,255,.75);color:#fff}
.tab{position:absolute;top:14px;height:24px;border-radius:8px;font-size:11px;font-weight:600;display:flex;align-items:center;justify-content:center}
.tab.on{background:var(--mauve);color:#fff}
.tab.off{border:1px solid var(--line);color:var(--ink)}
.legend{position:absolute;left:20px;top:52px;font-size:7.5px;color:#bbb;display:flex;gap:10px}
.legend i{display:inline-block;width:5px;height:5px;border-radius:50%;margin-right:4px}
.support{position:absolute;left:681px;top:353px;width:179px;height:239px;background:var(--mauve-soft);border-radius:8px}
.arch{position:absolute;left:703px;top:318px;width:135px;height:156px;border-radius:68px 68px 0 0;border:3px solid #fff;background:linear-gradient(160deg,#b3cde6 0%,#f48fb8 45%,#f27aa9 100%)}
.support-text{position:absolute;left:681px;width:179px;text-align:center;color:#fff}
.start-btn{position:absolute;left:731px;top:541px;width:79px;height:23px;background:var(--mauve-dark);border-radius:7px;color:#fff;font-size:12px;font-weight:600;display:flex;align-items:center;justify-content:center}
/* tasks */
.day{position:absolute;left:141px;width:735px;height:26px;background:var(--blue);color:#fff;font-size:12px;font-weight:600;display:flex;align-items:center;justify-content:space-between;padding:0 15px}
.day b{font-weight:600;margin-right:14px}
.task-time{position:absolute;left:141px;font-size:8px;color:#666}
.task{position:absolute;left:185px;width:691px;height:79px;background:#fff;border-radius:6px;box-shadow:0 2px 7px rgba(0,0,0,.12);overflow:hidden}
.task-head{height:24px;background:var(--pink-pale);display:flex;align-items:center;justify-content:space-between;padding:0 15px;font-size:8px;color:#555}
.task-head .type{display:flex;align-items:center;gap:5px}
.task-head .acts span{text-decoration:underline;margin-left:9px}
.task-body{position:relative;height:55px}
.task-person{position:absolute;left:15px;top:9px;font-size:12.5px;font-weight:600}
.task-project{position:absolute;left:165px;top:9px;font-size:12.5px;font-weight:600}
.task-desc{position:absolute;left:15px;top:31px;font-size:9px;color:#555}
.task-dur{position:absolute;right:0;top:0;width:100px;height:55px;border-left:1px solid var(--line);text-align:center;padding-top:6px}
.task-dur .big{font-size:18px;font-weight:500;letter-spacing:1px}
.task-dur .units{font-size:8.5px;color:#666;word-spacing:14px}
.fade{position:absolute;left:78px;top:1195px;width:862px;height:120px;background:linear-gradient(rgba(255,255,255,.3),rgba(255,255,255,.9) 55%,#fff)}
</style>
</head>
<body>
<main class="app">

  <!-- sidebar -->
  <aside class="sidebar">
    <div class="nav-active"></div>
    <svg class="nav-icon" style="top:42px" viewBox="0 0 24 24"><circle cx="12" cy="12" r="10" fill="#bf86a9"/><path d="M12 6v6l3 2" stroke="#fff" stroke-width="2" fill="none" stroke-linecap="round"/></svg>
    <svg class="nav-icon" style="top:101px" viewBox="0 0 24 24"><path d="M11 3a9 9 0 1 0 9 10h-9z" fill="#fff"/><path d="M13 1v10h10A10 10 0 0 0 13 1z" fill="#fff"/></svg>
    <div class="nav-sep" style="top:143px"></div>
    <svg class="nav-icon" style="top:159px" viewBox="0 0 24 24"><rect x="2" y="2" width="20" height="20" rx="4" fill="#fff"/><path d="M5 8l2 2 3-3M5 15l2 2 3-3" stroke="#bf86a9" stroke-width="1.8" fill="none"/><path d="M12 9h7M12 16h7" stroke="#bf86a9" stroke-width="1.8"/></svg>
    <div class="nav-sep" style="top:201px"></div>
    <svg class="nav-icon" style="top:218px" viewBox="0 0 24 24"><circle cx="12" cy="7" r="5" fill="#fff"/><path d="M3 23a9 8 0 0 1 18 0z" fill="#fff"/></svg>
    <svg class="nav-icon" style="top:1193px" viewBox="0 0 24 24"><path d="M12 1l2 3 3.5-1 .5 3.5 3.5 1-1.5 3.5 1.5 3-3.5 1-.5 3.5-3.5-1-2 3-2-3-3.5 1-.5-3.5-3.5-1L3 12 1.5 8.5 5 7.5l.5-3.5L9 5z" fill="#fff"/><circle cx="12" cy="12" r="4" fill="#bf86a9"/></svg>
    <div class="nav-sep" style="top:1235px"></div>
    <svg class="nav-icon" style="top:1255px" viewBox="0 0 24 24"><rect x="2" y="2" width="12" height="20" rx="3" fill="#fff"/><path d="M11 12h11M18 8l4 4-4 4" stroke="#fff" stroke-width="2.2" fill="none"/><circle cx="8" cy="12" r="1.3" fill="#bf86a9"/></svg>
  </aside>

  <!-- track your time -->
  <h2 class="section-title" style="left:141px;top:24px">Track your time</h2>
  <div class="dashed-btn" style="left:777px;top:22px;width:99px;height:24px">
    <svg width="10" height="10" viewBox="0 0 10 10"><rect width="10" height="10" rx="1.5" fill="#bf86a9"/><rect x="2" y="1" width="5" height="3" fill="#fff"/></svg>Save
  </div>

  <section class="card calendar" style="left:141px;top:62px;width:195px;height:213px">
    <div class="cal-arrow" style="left:14px"><svg width="22" height="26" viewBox="0 0 22 26"><path d="M13 8l-5 5 5 5" stroke="#aaa" fill="none"/></svg></div>
    <div class="cal-head">28 Oct</div>
    <div class="cal-arrow" style="left:158px;border:none"><svg width="22" height="26" viewBox="0 0 22 26"><path d="M9 8l5 5-5 5" stroke="#aaa" fill="none"/></svg></div>
    <div class="cal-grid">
      <span class="wd">Mon</span><span class="wd">Tue</span><span class="wd">Wed</span><span class="wd">Thu</span><span class="wd">Fri</span><span class="wd">Sat</span><span class="wd">Sun</span>
      <span class="out">25</span><span class="out">26</span><span class="out">27</span><span class="out">28</span><span class="out">29</span><span class="out">30</span><span>1</span>
      <span>2</span><span>3</span><span>4</span><span>5</span><span>6</span><span>7</span><span>8</span>
      <span>9</span><span>10</span><span>11</span><span>12</span><span>13</span><span>14</span><span>15</span>
      <span>16</span><span>17</span><span>18</span><span>19</span><span>20</span><span>21</span><span>22</span>
      <span>23</span><span>24</span><span>25</span><span>26</span><span>27</span><span class="today">28</span><span>29</span>
      <span>30</span><span>31</span><span class="out">1</span><span class="out">2</span><span class="out">3</span><span class="out">4</span><span class="out">5</span>
    </div>
  </section>

  <section class="card duration" style="left:351px;top:62px;width:195px;height:213px;overflow:hidden">
    <div class="chip" style="left:15px;top:16px">1 h</div>
    <div class="chip on" style="left:59px;top:16px">2 h</div>
    <div class="chip" style="left:103px;top:16px">3 h</div>
    <div class="chip" style="left:147px;top:16px">4 h</div>
    <div class="chip" style="left:15px;top:60px">5 h</div>
    <div class="chip" style="left:59px;top:60px">6 h</div>
    <div class="chip" style="left:103px;top:60px">7 h</div>
    <div class="chip" style="left:147px;top:60px">8 h</div>
    <div class="minutes-band"></div>
    <div class="chip" style="left:15px;top:111px">0 m</div>
    <div class="chip" style="left:59px;top:111px">15 m</div>
    <div class="chip on" style="left:103px;top:111px">30 m</div>
    <div class="chip" style="left:147px;top:111px">45 m</div>
    <div class="total" style="top:160px"><div class="big">2&nbsp;&nbsp;:&nbsp;&nbsp;30</div><div class="units">hours&nbsp;&nbsp;&nbsp;&nbsp;&nbsp;&nbsp;&nbsp;&nbsp;&nbsp;&nbsp;&nbsp;minutes</div></div>
  </section>

  <section class="card entry-form" style="left:561px;top:62px;width:315px;height:213px">
    <div class="select" style="left:15px;width:138px">Select Project<svg width="14" height="8" viewBox="0 0 14 8"><path d="M1 1l6 6 6-6" stroke="#999" fill="none"/></svg></div>
    <div class="select" style="left:163px;width:138px">Select Type<svg width="14" height="8" viewBox="0 0 14 8"><path d="M1 1l6 6 6-6" stroke="#999" fill="none"/></svg></div>
    <div class="note">What did you do?</div>
    <table class="log">
      <tr><th>Time</th><th>Customer</th><th>Project</th><th>Type</th></tr>
      <tr><td>15.00 pm</td><td>Quentin Richardson</td><td>Project 1</td><td>&lt;/&gt; Coding</td></tr>
      <tr><td>10.35 am</td><td>Jayson Newton</td><td>Project 2</td><td>▭ Meeting</td></tr>
      <tr><td>9.15 am</td><td>Teresa Wells</td><td>Project 3</td><td>▣ Project Men...</td></tr>
      <tr><td>9.00 am</td><td>Gillian Foster</td><td>Project 4</td><td>&lt;/&gt; Coding</td></tr>
    </table>
  </section>

  <!-- statistic -->
  <div class="stat-band"></div>
  <h2 class="section-title stat-title" style="left:141px;top:321px">Statistic</h2>
  <div class="dashed-btn light" style="left:567px;top:318px;width:99px;height:24px">Show all</div>

  <section class="card chart" style="left:141px;top:353px;width:524px;height:239px">
    <div class="tab on" style="left:14px;width:127px">Current month</div>
    <div class="tab off" style="left:152px;width:126px">Last month</div>
    <div class="select" style="left:422px;top:12px;width:88px;height:24px;font-weight:500">Monate<svg width="14" height="8" viewBox="0 0 14 8"><path d="M1 1l6 6 6-6" stroke="#999" fill="none"/></svg></div>
    <div class="legend"><span>%</span><span>Comleted Projects:</span><span><i style="background:var(--pink-light)"></i>0-24%</span><span><i style="background:var(--pink-light)"></i>25-49%</span><span><i style="background:var(--pink)"></i>50-74%</span><span><i style="background:var(--mauve)"></i>75-100%</span></div>
    <svg class="abs" style="left:0;top:0" width="524" height="239" viewBox="0 0 524 239" font-family="Inter, sans-serif">
      <line x1="14" y1="66" x2="510" y2="66" stroke="#e6e6e6"/>
      <g stroke="#eee"><line x1="40" y1="87" x2="510" y2="87"/><line x1="40" y1="118" x2="510" y2="118"/><line x1="40" y1="149" x2="510" y2="149"/><line x1="40" y1="180" x2="510" y2="180"/><line x1="40" y1="212" x2="510" y2="212"/></g>
      <g font-size="8" fill="#444" text-anchor="end"><text x="35" y="90">100%</text><text x="35" y="121">75%</text><text x="35" y="152">50%</text><text x="35" y="183">25%</text><text x="35" y="215">0%</text></g>
      <g>
        <rect x="50" y="192" width="18" height="20" rx="2" fill="#fde4ee"/>
        <rect x="79" y="187" width="18" height="25" rx="2" fill="#fde4ee"/>
        <rect x="109" y="124" width="18" height="88" rx="2" fill="#f48fb8"/>
        <rect x="138" y="156" width="18" height="56" rx="2" fill="#fbc4d8"/>
        <rect x="168" y="93" width="18" height="119" rx="2" fill="#bf86a9"/>
        <rect x="197" y="142" width="18" height="70" rx="2" fill="#f48fb8"/>
        <rect x="226" y="172" width="18" height="40" rx="2" fill="#fbc4d8"/>
        <rect x="256" y="193" width="18" height="19" rx="2" fill="#fbc4d8"/>
        <rect x="285" y="132" width="18" height="80" rx="2" fill="#f48fb8"/>
        <rect x="315" y="162" width="18" height="50" rx="2" fill="#fbc4d8"/>
        <rect x="344" y="157" width="18" height="55" rx="2" fill="#fbc4d8"/>
        <rect x="373" y="140" width="18" height="72" rx="2" fill="#f48fb8"/>
        <rect x="403" y="116" width="18" height="96" rx="2" fill="#bf86a9"/>
        <rect x="432" y="147" width="18" height="65" rx="2" fill="#f48fb8"/>
        <rect x="461" y="137" width="18" height="75" rx="2" fill="#f48fb8"/>
      </g>
      <g font-size="7.5" font-weight="600" text-anchor="middle">
        <text x="59" y="189" fill="#fbc4d8">16%</text><text x="88" y="184" fill="#fbc4d8">20%</text>
        <text x="118" y="121" fill="#f48fb8">70%</text><text x="147" y="153" fill="#fbc4d8">45%</text>
        <text x="177" y="90" fill="#bf86a9">95%</text><text x="206" y="139" fill="#f48fb8">56%</text>
        <text x="235" y="169" fill="#fbc4d8">32%</text><text x="265" y="190" fill="#fbc4d8">15%</text>
        <text x="294" y="129" fill="#f48fb8">64%</text>
        <text x="412" y="113" fill="#bf86a9">77%</text><text x="441" y="144" fill="#f48fb8">52%</text>
        <text x="470" y="134" fill="#f48fb8">60%</text>
      </g>
      <g font-size="8" fill="#444" text-anchor="middle">
        <text x="59" y="227">1</text><text x="88" y="227">2</text><text x="118" y="227">3</text><text x="147" y="227">4</text><text x="177" y="227">5</text><text x="206" y="227">6</text><text x="235" y="227">7</text><text x="265" y="227">8</text><text x="294" y="227" font-weight="700" fill="#222">9</text><text x="324" y="227">10</text><text x="353" y="227">11</text><text x="382" y="227">12</text><text x="412" y="227">13</text><text x="441" y="227">14</text><text x="470" y="227">15</text>
      </g>
      <g>
        <rect x="315" y="125" width="68" height="26" rx="3" fill="#fff" stroke="#eee"/>
        <text x="323" y="136" font-size="7.5" font-weight="600" fill="#222">Q. Richardson</text>
        <text x="323" y="146" font-size="7" fill="#777">Project 1</text>
        <path d="M297 168l0 16 4-4 3 7 3-1-3-7 5 0z" fill="#fff" stroke="#999" stroke-width=".6"/>
      </g>
    </svg>
  </section>

  <div class="support"></div>
  <div class="arch" role="img" aria-label="Playful illustration of a hand holding a magnifying glass with sparkles"></div>
  <div class="support-text" style="top:496px;font-size:17px;font-weight:700">Support 24/7</div>
  <div class="support-text" style="top:521px;font-size:8.5px">Contact us anytime</div>
  <div class="start-btn">Start</div>

  <!-- tasks -->
  <h2 class="section-title" style="left:141px;top:638px">Your tasks</h2>
  <div class="dashed-btn" style="left:774px;top:637px;width:98px;height:24px">
    <svg width="11" height="10" viewBox="0 0 11 10" stroke="#bf86a9" stroke-width="1.3"><path d="M0 2h11M0 5h11M0 8h11"/><circle cx="3" cy="2" r="1.3" fill="#fff"/><circle cx="7" cy="5" r="1.3" fill="#fff"/><circle cx="4" cy="8" r="1.3" fill="#fff"/></svg>Filter
  </div>

  <div class="day" style="top:676px"><span><b>Wednesday</b>October 25th</span><span>4 hours 30 minutes</span></div>
  <div class="task-time" style="top:754px">09.00 am</div>
  <article class="task" style="top:718px">
    <div class="task-head"><span class="type">&lt;/&gt; Coding</span><span class="acts"><span>Delete</span><span>Edit</span></span></div>
    <div class="task-body"><span class="task-person">Jayson Newton</span><span class="task-project">Project 1</span><span class="task-desc">Some description what the user did on that project</span><div class="task-dur"><div class="big">4&nbsp;&nbsp;:&nbsp;&nbsp;30</div><div class="units">hours minutes</div></div></div>
  </article>

  <div class="day" style="top:818px"><span><b>Thuesday</b>October 24th</span><span>7 hours 45 minutes</span></div>
  <div class="task-time" style="top:896px">15.00 pm</div>
  <article class="task" style="top:860px">
    <div class="task-head"><span class="type">▭ Meeting</span><span class="acts"><span>Delete</span><span>Edit</span></span></div>
    <div class="task-body"><span class="task-person">Teresa Wells</span><span class="task-project">Project 1</span><span class="task-desc">Some description what the user did on that project</span><div class="task-dur"><div class="big">0&nbsp;&nbsp;:&nbsp;&nbsp;30</div><div class="units">hours minutes</div></div></div>
  </article>
  <div class="task-time" style="top:995px">11.00 am</div>
  <article class="task" style="top:959px">
    <div class="task-head"><span class="type">▣ Project Management</span><span class="acts"><span>Delete</span><span>Edit</span></span></div>
    <div class="task-body"><span class="task-person">Quentin Richardson</span><span class="task-project">Project 1</span><span class="task-desc">Some description what the user did on that project</span><div class="task-dur"><div class="big">2&nbsp;&nbsp;:&nbsp;&nbsp;45</div><div class="units">hours minutes</div></div></div>
  </article>
  <div class="task-time" style="top:1094px">09.00 am</div>
  <article class="task" style="top:1058px">
    <div class="task-head"><span class="type">&lt;/&gt; Coding</span><span class="acts"><span>Delete</span><span>Edit</span></span></div>
    <div class="task-body"><span class="task-person">Jayson Newton</span><span class="task-project">Project 1</span><span class="task-desc">Some description what the user did on that project</span><div class="task-dur"><div class="big">4&nbsp;&nbsp;:&nbsp;&nbsp;30</div><div class="units">hours minutes</div></div></div>
  </article>

  <div class="day" style="top:1159px"><span><b>Monday</b>October 23th</span><span>3 hours 15 minutes</span></div>
  <div class="task-time" style="top:1237px">09.00 am</div>
  <article class="task" style="top:1201px">
    <div class="task-head"><span class="type">▣ Project Management</span><span class="acts"><span>Delete</span><span>Edit</span></span></div>
    <div class="task-body"><span class="task-person">Teresa Wells</span><span class="task-project">Project 1</span><span class="task-desc">Some description what the user did on that project</span><div class="task-dur"><div class="big">3&nbsp;&nbsp;:&nbsp;&nbsp;15</div><div class="units">hours minutes</div></div></div>
  </article>
  <div class="fade"></div>
</main>
</body>
</html>
```